Mortgage Loan Program(s) for Furloughed Federal Government Workers

Mortgage Loan Program(s)
For
Furloughed Federal Government Workers

* Preserve Your Credit Rating
* Receive Cash out to Increase Savings or Consolidate Bills
* Close in 30 Days or Less
* FHA and Conventional Loan Programs
* Very Competitive Rates Available
* DC & MD Properties Only

You deserve better. Contact us today....

Office (800) 647-2914 x23
Cell (240) 486-2079
Email mkowalczyk@brightpathlending.example

Marcus Kowalczyk
Brightpath Lending Services, Inc.
NMLS #837160 / #56408

Target Market(s)

```html
<!DOCTYPE html>
<html lang="en">
<head>
<meta charset="utf-8">
<title>Mortgage Loan Programs for Furloughed Federal Government Workers</title>
<link rel="stylesheet" href="https://fonts.googleapis.com/css2?family=Montserrat:wght@400;500;700;800&family=Oswald:wght@500&display=swap">
<style>
  :root {
    --gold: #b09b2c;
    --gold-soft: #cdc39c;
    --blue: #0b5ea8;
    --blue-dark: #0d4f8e;
    --grey-band: #a9a9a9;
    --grey-arrow: #8c8c8c;
    --paper: #f2f2f2;
    --ink: #555555;
    --white: #ffffff;
  }
  * { margin: 0; padding: 0; box-sizing: border-box; }
  html, body { width: 861px; height: 1200px; overflow: hidden; background: var(--paper); }
  .flyer { position: relative; width: 861px; height: 1200px; background: linear-gradient(180deg, #f7f7f7, #ececec); font-family: "Montserrat", sans-serif; }

  .hero { position: absolute; left: 0; top: 0; width: 861px; height: 237px; display: block; }

  .title-band { position: absolute; left: 0; top: 237px; width: 861px; height: 101px; background: var(--gold); text-align: center; padding-top: 18px; }
  .title-band h1 { color: var(--white); font-weight: 800; font-size: 39px; letter-spacing: 1px; line-height: 1; }
  .title-band p { color: var(--blue); font-weight: 500; font-size: 24px; letter-spacing: 2.2px; margin-top: 4px; line-height: 1; }

  .rule { position: absolute; left: 62px; top: 344px; width: 748px; height: 1px; background: #d6d6d6; }

  .benefits { list-style: none; }
  .benefit { position: absolute; left: 0; height: 52px; }
  .benefit-num { position: absolute; left: 68px; top: -10px; width: 50px; text-align: center; font-size: 66px; font-weight: 500; color: var(--gold-soft); line-height: 1; }
  .benefit-ribbon { position: absolute; left: 143px; top: 0; height: 52px; background: var(--blue); color: var(--white); font-family: "Oswald", sans-serif; font-weight: 500; font-size: 22px; line-height: 52px; padding-left: 16px; text-transform: uppercase; }
  .benefit-tab { position: absolute; top: 44px; width: 50px; height: 44px; }

  .contact-band { position: absolute; left: 0; top: 941px; width: 861px; height: 73px; background: var(--grey-band); }
  .contact-band p { position: absolute; right: 14px; top: 24px; font-weight: 700; font-size: 23px; letter-spacing: 0.3px; color: var(--white); }
  .contact-band .accent { color: var(--blue); }

  .agent-photo { position: absolute; left: 41px; top: 892px; width: 206px; height: 200px; border: 3px solid var(--blue); background: linear-gradient(160deg, #3b5d86, #1f2b3d 70%); }

  .agent { position: absolute; left: 38px; top: 1094px; color: var(--ink); }
  .agent-name { font-size: 23px; font-weight: 700; line-height: 1.1; }
  .agent-meta { font-size: 15px; line-height: 1.45; margin-top: 2px; }

  .brand { position: absolute; left: 330px; top: 1086px; width: 200px; display: flex; align-items: center; gap: 8px; }
  .brand-mark { width: 22px; height: 22px; border-radius: 50%; background: var(--gold); flex: none; }
  .brand-name { font-size: 19px; font-weight: 700; color: var(--blue); line-height: 1.15; }

  .contact { position: absolute; right: 36px; top: 1101px; text-align: right; color: var(--ink); font-size: 15px; line-height: 20px; }
  .contact li { list-style: none; display: flex; justify-content: flex-end; align-items: center; gap: 5px; }
  .contact svg { width: 16px; height: 14px; fill: var(--blue); }
</style>
</head>
<body>
<main class="flyer">
  <svg class="hero" viewBox="0 0 861 237">
    <defs>
      <linearGradient id="heroWarm" x1="0" y1="0" x2="1" y2="1">
        <stop offset="0" stop-color="#a9a6a2"/><stop offset="1" stop-color="#6e6358"/>
      </linearGradient>
      <linearGradient id="heroCool" x1="0" y1="0" x2="1" y2="1">
        <stop offset="0" stop-color="#b8b4ad"/><stop offset="1" stop-color="#7d7064"/>
      </linearGradient>
    </defs>
    <rect width="861" height="237" fill="#ffffff"/>
    <polygon points="0,0 550,0 472,237 0,237" fill="url(#heroWarm)" role="img" aria-label="Couple reviewing household paperwork together"/>
    <polygon points="565,0 861,0 861,237 487,237" fill="url(#heroCool)" role="img" aria-label="Stressed couple with bills and a help sign"/>
  </svg>

  <header class="title-band">
    <h1>MORTGAGE LOAN PROGRAM(S)</h1>
    <p>FOR FURLOUGHED FEDERAL GOVERNMENT WORKERS</p>
  </header>

  <div class="rule"></div>

  <ol class="benefits">
    <li class="benefit" style="top:374px">
      <span class="benefit-num">1</span>
      <span class="benefit-ribbon" style="width:394px">DC &amp; MD Properties Only</span>
      <svg class="benefit-tab" style="left:491px" viewBox="0 0 50 44"><polygon points="0,0 46,0 26,34" fill="var(--grey-arrow)"/></svg>
    </li>
    <li class="benefit" style="top:466px">
      <span class="benefit-num">2</span>
      <span class="benefit-ribbon" style="width:463px">Close in 30 Days or Less</span>
      <svg class="benefit-tab" style="left:560px" viewBox="0 0 50 44"><polygon points="0,0 46,0 26,34" fill="var(--grey-arrow)"/></svg>
    </li>
    <li class="benefit" style="top:556px">
      <span class="benefit-num">3</span>
      <span class="benefit-ribbon" style="width:500px">Preserve Your Credit Rating</span>
      <svg class="benefit-tab" style="left:597px" viewBox="0 0 50 44"><polygon points="0,0 46,0 26,34" fill="var(--grey-arrow)"/></svg>
    </li>
    <li class="benefit" style="top:647px">
      <span class="benefit-num">4</span>
      <span class="benefit-ribbon" style="width:557px">Very Competitive Rates Available</span>
      <svg class="benefit-tab" style="left:654px" viewBox="0 0 50 44"><polygon points="0,0 46,0 26,34" fill="var(--grey-arrow)"/></svg>
    </li>
    <li class="benefit" style="top:738px">
      <span class="benefit-num">5</span>
      <span class="benefit-ribbon" style="width:605px">FHA and Conventional Loan Programs</span>
      <svg class="benefit-tab" style="left:702px" viewBox="0 0 50 44"><polygon points="0,0 46,0 26,34" fill="var(--grey-arrow)"/></svg>
    </li>
    <li class="benefit" style="top:829px">
      <span class="benefit-num">6</span>
      <span class="benefit-ribbon" style="width:657px">Receive Cash Out to Increase Savings or Consolidate Bills</span>
      <svg class="benefit-tab" style="left:754px" viewBox="0 0 50 44"><polygon points="0,0 46,0 26,34" fill="var(--grey-arrow)"/></svg>
    </li>
  </ol>

  <section class="contact-band">
    <p><span class="accent">YOU DESERVE BETTER</span> CONTACT US TODAY</p>
  </section>

  <div class="agent-photo" role="img" aria-label="Portrait of loan officer Marcus Kowalczyk in a dark suit"></div>

  <div class="agent">
    <div class="agent-name">Marcus Kowalczyk</div>
    <div class="agent-meta">Brightpath Lending Services, Inc.<br>NMLS #837160 / #56408</div>
  </div>

  <div class="brand">
    <span class="brand-mark"></span>
    <span class="brand-name">Brightpath Lending</span>
  </div>

  <ul class="contact">
    <li><svg viewBox="0 0 16 14"><path d="M1 5 Q8 -1 15 5 L13 7 L11 5.5 L11 4 Q8 3 5 4 L5 5.5 L3 7 Z M4 7 H12 L14 13 H2 Z"/></svg>(800) 647-2914 x23</li>
    <li><svg viewBox="0 0 16 14"><path d="M4 0 L7 3 L5.5 5 Q7 8.5 9.5 10 L11.5 8.5 L14 11.5 L12 14 Q4 12 2 2 Z"/></svg>(240) 486-2079</li>
    <li><svg viewBox="0 0 16 14"><path d="M1 3 H15 V12 H1 Z M1 3 L8 8 L15 3" fill="var(--blue)" stroke="#ffffff" stroke-width="1"/></svg>mkowalczyk@brightpathlending.example</li>
  </ul>
</main>
</body>
</html>
```